Label design

I am looking for a designer for 6 polish pot labels. Free to propose to me the best design, quite chic, sophisticated and in the era of the time, I put a Varexin label and a Coltrusa label that I see well in the files. Dimension 32cm long by 11cm high. These are labels for round paint pots. (example of our current varnish pots in the files). The 6 different varnishes are: - marine varnish (varnish yacht) - varnish for wood (varnish varnish) - varnish for stone (stone varnish) - rust varnish (varnish anti-rust) - varnish kitchen and bathroom (kitchen & bathroom varnish) ) - varnish for metal (metal varnish) The elements to be present on the front are: - LOGO (available attached) - IMAGE REPRESENTATIVE preferably on the top half of the label - Name in English (subtitled in French ) - COLORLESS - POLYVINYL RESIN - HIGH QUALITY - and a small logo "made in France" The elements to be present behind: indication (see image) to know: --rendement 12m2 / L - 30 minutes dry touch - 8h between two layers --material: roll and brush

```html
<!DOCTYPE html>
<html lang="en">
<head>
<meta charset="utf-8">
<title>Kitchen &amp; Bathroom Varnish Label</title>
<link href="https://fonts.googleapis.com/css2?family=Open+Sans:ital,wdth,wght@0,75..100,400..800;1,75..100,400..800&family=Libre+Baskerville&display=swap" rel="stylesheet">
<style>
  :root {
    --backdrop-top: #9a9a9a;
    --backdrop-bottom: #6f6f6f;
    --teal: #11908f;
    --teal-deep: #0b7a7c;
    --sky-blue: #169fd9;
    --white: #ffffff;
  }
  html, body {
    margin: 0;
    padding: 0;
    width: 683px;
    height: 1200px;
    overflow: hidden;
  }
  body {
    background: linear-gradient(180deg, var(--backdrop-top), var(--backdrop-bottom));
    position: relative;
  }
  .label {
    position: absolute;
    left: 31px;
    top: 387px;
    width: 620px;
    height: 426px;
    overflow: hidden;
    box-shadow: 0 6px 18px rgba(0,0,0,0.35);
  }
  .label-art {
    position: absolute;
    inset: 0;
    width: 620px;
    height: 426px;
  }
  .brand-name {
    position: absolute;
    left: 150px;
    top: 260px;
    width: 265px;
    margin: 0;
    text-align: center;
    font-family: "Open Sans", sans-serif;
    font-weight: 800;
    font-stretch: 75%;
    font-size: 34px;
    letter-spacing: -0.5px;
    color: var(--white);
    line-height: 1.1;
    white-space: nowrap;
  }
  .tagline {
    position: absolute;
    left: 300px;
    top: 305px;
    width: 152px;
    margin: 0;
    text-align: right;
    font-family: "Open Sans", sans-serif;
    font-style: italic;
    font-weight: 400;
    font-size: 15px;
    line-height: 1.2;
    color: var(--white);
    white-space: nowrap;
  }
  .product-name {
    position: absolute;
    left: 0;
    top: 337px;
    width: 620px;
    margin: 0;
    text-align: center;
    font-family: "Libre Baskerville", serif;
    font-weight: 400;
    font-size: 25px;
    line-height: 1.2;
    letter-spacing: 0.3px;
    color: var(--white);
    text-transform: uppercase;
    white-space: nowrap;
  }
  .product-features {
    position: absolute;
    left: 0;
    top: 387px;
    width: 620px;
    height: 27px;
    margin: 0;
    padding: 0;
    list-style: none;
    display: flex;
    justify-content: center;
    align-items: center;
    font-family: "Open Sans", sans-serif;
    font-weight: 700;
    font-size: 16px;
    color: var(--white);
    white-space: nowrap;
  }
  .product-features li + li::before {
    content: "";
    display: inline-block;
    width: 1.5px;
    height: 14px;
    background: var(--white);
    margin: 0 12px;
    vertical-align: -1px;
  }
</style>
</head>
<body>
  <section class="label">
    <svg class="label-art" viewBox="0 0 620 426" xmlns="http://www.w3.org/2000/svg">
      <defs>
        <linearGradient id="photo-tones" x1="0" y1="0" x2="1" y2="1">
          <stop offset="0" stop-color="#6b5444"/>
          <stop offset="0.35" stop-color="#b9b2a6"/>
          <stop offset="0.6" stop-color="#e2ddd4"/>
          <stop offset="0.8" stop-color="#8e7a68"/>
          <stop offset="1" stop-color="#d6dccf"/>
        </linearGradient>
        <linearGradient id="teal-field" x1="0" y1="0" x2="0" y2="1">
          <stop offset="0" stop-color="var(--teal)"/>
          <stop offset="1" stop-color="var(--teal-deep)"/>
        </linearGradient>
        <linearGradient id="swoosh-shine" x1="0" y1="0" x2="1" y2="0">
          <stop offset="0" stop-color="#ffffff"/>
          <stop offset="0.6" stop-color="#e8eef0"/>
          <stop offset="1" stop-color="#b8c6cc"/>
        </linearGradient>
      </defs>

      <rect class="teal-field" x="0" y="0" width="620" height="426" fill="url(#teal-field)"/>

      <path class="photo-area" role="img" aria-label="Photo of a modern kitchen with dark wood cabinets, a granite island and a steel range"
            d="M0 0 H620 V160 C520 164 420 184 330 214 C250 240 160 244 0 186 Z"
            fill="url(#photo-tones)"/>

      <path class="blue-swoosh"
            d="M330 214 C420 184 520 164 620 160 V140 C520 146 420 170 330 214 Z"
            fill="var(--sky-blue)"/>

      <path class="white-swoosh"
            d="M0 186 C160 244 250 240 330 214 C420 184 520 164 620 160 V168 C520 172 425 192 335 222 C250 250 150 252 0 202 Z"
            fill="url(#swoosh-shine)"/>

      <circle class="origin-badge" cx="481" cy="266" r="40" fill="var(--white)"/>
      <circle cx="481" cy="266" r="32" fill="#d8e2ea"/>

      <rect class="feature-band" x="0" y="387" width="620" height="27" fill="var(--sky-blue)"/>
    </svg>

    <h1 class="brand-name">Brellon Coatings</h1>
    <p class="tagline">Quality or nothing</p>
    <h2 class="product-name">Kitchen &amp; Bathroom Varnish</h2>
    <ul class="product-features">
      <li>COLORLESS</li>
      <li>POLYVINYL RESIN</li>
      <li>HIGH QUALITY</li>
    </ul>
  </section>
</body>
</html>
```